PowerPoint template for project mangement course material

I need a ppt template for the slides at our project management course. IT should be arather simple adn stylish not taking the focus away from the content. We are two companies delivering the course - thus the template should be held in the colours of the two companies and their logos. we need different layouts for the template - the logos should be included in minimum the title layout.
The content is a mix of text and figures.
(uploaded ppt shows an example of the content)

Industry/Entity Type

Training

Font styles to use
Serif
Sans Serif

Requirements
Must have
• different layouts: title, section, standard, two columns, headline only etc.
Nice to have
• nice bullets, mostly white background

```html
<!DOCTYPE html>
<html lang="da">
<head>
<meta charset="utf-8">
<title>Projektledelse – slide template</title>
<link rel="stylesheet" href="https://fonts.googleapis.com/css2?family=Carlito:ital,wght@0,400;0,700;1,700&family=Open+Sans:wght@300;400&display=swap">
<style>
  :root {
    --navy: #0b3a5f;
    --navy-deep: #08365a;
    --red: #a33a33;
    --red-mark: #b23a30;
    --black: #000000;
    --white: #ffffff;
    --ink: #1e1e1e;
    --grey-text: #5a5a5a;
    --grey-rule: #8c8c8c;
    --footer-band: #f1f1f1;
    --gutter: #c9c9c9;
  }
  * { margin: 0; padding: 0; box-sizing: border-box; }
  html, body { width: 1200px; height: 2235px; overflow: hidden; background: var(--gutter); }
  body { position: relative; font-family: "Carlito", "Calibri", sans-serif; color: var(--ink); }
  h1, h2, p { font-weight: 400; }

  .slide { position: absolute; width: 598px; height: 445px; overflow: hidden; background: var(--white); }
  .col-a { left: 0; } .col-b { left: 602px; }
  .row-1 { top: 0; } .row-2 { top: 447px; } .row-3 { top: 894px; } .row-4 { top: 1341px; } .row-5 { top: 1788px; }

  .abs { position: absolute; }
  .rule { position: absolute; height: 1px; background: var(--grey-rule); }
  .rule.light { background: rgba(255,255,255,.75); }

  /* wordmark pair */
  .brand-pair { position: absolute; display: flex; align-items: center; gap: 10px; }
  .brand { display: flex; align-items: center; gap: 5px; font-family: "Carlito", sans-serif; font-weight: 400; line-height: 1; white-space: nowrap; }
  .brand-mark { flex: none; }
  .brand-a { color: var(--navy); }
  .brand-a .brand-mark { background: var(--navy); border-radius: 50%; }
  .brand-b { color: var(--grey-text); }
  .brand-b .brand-mark { background: var(--grey-text); }
  .brand-divider { width: 1px; background: var(--grey-rule); align-self: stretch; }
  .brand-pair.lg .brand { font-size: 16px; } .brand-pair.lg .brand-mark { width: 12px; height: 12px; }
  .brand-pair.sm .brand { font-size: 7px; gap: 3px; } .brand-pair.sm .brand-mark { width: 6px; height: 6px; }
  .brand-pair.sm { gap: 6px; }

  /* title slides */
  .main-title { font-family: "Open Sans", sans-serif; font-weight: 300; font-size: 26px; color: var(--ink); }
  .sub-red { font-size: 11px; color: var(--red); }
  .bullet-sub::before { content: "•"; margin-right: 8px; }
  .cover-title { font-family: "Open Sans", sans-serif; font-weight: 400; font-size: 17px; color: var(--ink); }

  /* section slides */
  .section-title { font-family: "Open Sans", sans-serif; font-weight: 400; font-size: 20px; color: var(--white); white-space: nowrap; }
  .bg-red { background: var(--red); } .bg-navy { background: var(--navy-deep); } .bg-black { background: var(--black); }
  .photo-fill { position: absolute; inset: 0; background: linear-gradient(160deg, #3f5f7f 0%, #24507a 35%, #1d4b74 60%, #16416a 100%); }

  /* content slides */
  .accent-bar { position: absolute; left: 0; top: 0; width: 7px; height: 40px; background: var(--red); }
  .slide-title { position: absolute; left: 30px; top: 16px; font-family: "Open Sans", sans-serif; font-weight: 400; font-size: 22px; color: var(--ink); }
  .page-no { position: absolute; right: 30px; top: 0; width: 25px; height: 27px; background: var(--red-mark); color: var(--white); font-size: 8px; display: flex; align-items: center; justify-content: center; }
  .footer { position: absolute; left: 0; right: 0; bottom: 0; height: 22px; background: var(--footer-band); }
  .footer-meta { position: absolute; right: 20px; top: 7px; font-size: 6px; color: var(--grey-text); display: flex; gap: 20px; font-family: "Open Sans", sans-serif; }

  .figure-frame { position: absolute; left: 160px; top: 70px; width: 277px; height: 328px; border: 3px solid var(--navy); background: var(--white); }
  .figure-art { position: absolute; left: 12px; top: 10px; right: 12px; height: 235px; background: linear-gradient(180deg, #f4f4f4, #d9d9d9); }
  .figure-caption { position: absolute; left: 32px; top: 248px; right: 14px; font-family: "Carlito", serif; font-size: 12px; line-height: 1.2; color: var(--ink); }
  .figure-caption strong { display: block; font-weight: 400; font-size: 14px; }

  .column { position: absolute; top: 112px; width: 225px; font-family: "Open Sans", sans-serif; font-size: 11.5px; color: var(--grey-text); }
  .column h3 { font-family: "Carlito", sans-serif; font-weight: 700; font-size: 13.5px; color: var(--navy); margin-bottom: 4px; }
  .column ul { list-style: none; }
  .column li { position: relative; padding-left: 16px; margin-bottom: 5px; line-height: 1.2; }
  .column li::before { content: ""; position: absolute; left: 0; top: 2px; width: 9px; height: 9px; border: 1.5px solid var(--navy); border-radius: 50%; box-shadow: inset 0 0 0 1.5px var(--white); background: var(--navy); }
  .column li.sub { padding-left: 44px; margin-bottom: 2px; }
  .column li.sub::before { left: 30px; top: 4px; width: 0; height: 0; border: none; border-left: 5px solid var(--navy); border-top: 3px solid transparent; border-bottom: 3px solid transparent; box-shadow: none; background: none; border-radius: 0; }
  .motto { margin-top: 14px; font-family: "Carlito", sans-serif; font-weight: 700; font-style: italic; font-size: 12.5px; color: var(--navy); }

  .thanks { font-family: "Open Sans", sans-serif; font-weight: 400; font-size: 19px; color: var(--navy); }
</style>
</head>
<body>

<!-- Title layout A -->
<section class="slide col-a row-1">
  <div class="brand-pair lg" style="right:28px; top:30px;">
    <span class="brand brand-a"><span class="brand-mark"></span>Vedel Rådgivning</span>
    <span class="brand-divider"></span>
    <span class="brand brand-b"><span class="brand-mark"></span>Nørlund Akademi</span>
  </div>
  <h1 class="main-title abs" style="left:18px; top:345px;">Your Presentation Title Here</h1>
  <div class="rule" style="left:18px; width:550px; top:383px;"></div>
  <p class="sub-red bullet-sub abs" style="left:18px; top:392px;">Your subtitle Here</p>
</section>

<!-- Title layout B -->
<section class="slide col-b row-1">
  <div class="brand-pair lg" style="left:150px; top:172px;">
    <span class="brand brand-a"><span class="brand-mark"></span>Vedel Rådgivning</span>
    <span class="brand-divider"></span>
    <span class="brand brand-b"><span class="brand-mark"></span>Nørlund Akademi</span>
  </div>
  <div class="rule" style="left:30px; width:330px; top:222px;"></div>
  <h1 class="cover-title abs" style="left:30px; top:239px;">Presentation Title Goes Here</h1>
  <p class="sub-red abs" style="left:30px; top:264px;">Your Subtitle Goes Here</p>
</section>

<!-- Welcome with photo -->
<section class="slide col-a row-2">
  <div class="photo-fill" role="img" aria-label="Blue-tinted street photograph with a truck and a traffic sign"></div>
  <h2 class="section-title abs" style="right:238px; top:190px;">Velkommen</h2>
  <div class="rule light" style="left:33px; width:330px; top:222px;"></div>
</section>

<!-- Standard width layout -->
<section class="slide col-b row-2">
  <div class="accent-bar"></div>
  <h2 class="slide-title">1 Standard width layout</h2>
  <div class="page-no">4</div>
  <figure class="figure-frame">
    <div class="figure-art" role="img" aria-label="Line drawing of a sailing ship"></div>
    <figcaption class="figure-caption"><strong>The Columbus model</strong>Do as Columbus: Decide on the goal of the journey and keep check on and adjust the direction continually in order to reach the goal in question.</figcaption>
  </figure>
  <footer class="footer">
    <div class="brand-pair sm" style="left:12px; top:7px;">
      <span class="brand brand-b"><span class="brand-mark"></span>Nørlund Akademi</span>
      <span class="brand brand-a"><span class="brand-mark"></span>Vedel Rådgivning</span>
    </div>
    <div class="footer-meta"><span>Projektledelse i praksis v. Anders Holm og Sofie Lund</span><span>28-06-2017</span></div>
  </footer>
</section>

<!-- Section red -->
<section class="slide col-a row-3 bg-red">
  <h2 class="section-title abs" style="left:95px; top:190px;">Your section Title Goes Here</h2>
  <div class="rule light" style="left:33px; width:330px; top:222px;"></div>
</section>

<!-- Section navy right -->
<section class="slide col-b row-3 bg-navy">
  <h2 class="section-title abs" style="left:233px; top:190px;">Your section Title Goes Here</h2>
  <div class="rule light" style="left:233px; width:334px; top:222px;"></div>
</section>

<!-- Section black framed -->
<section class="slide col-a row-4 bg-black">
  <div class="rule light" style="left:235px; width:332px; top:184px;"></div>
  <h2 class="section-title abs" style="left:235px; top:191px;">Your section Title Goes Here</h2>
  <div class="rule light" style="left:235px; width:332px; top:226px;"></div>
</section>

<!-- Section navy framed -->
<section class="slide col-b row-4 bg-navy">
  <div class="rule light" style="left:30px; width:332px; top:184px;"></div>
  <h2 class="section-title abs" style="left:97px; top:191px;">Your section Title Goes Here</h2>
  <div class="rule light" style="left:30px; width:332px; top:226px;"></div>
</section>

<!-- Two column text -->
<section class="slide col-a row-5">
  <div class="accent-bar"></div>
  <h2 class="slide-title">Two Column Text</h2>
  <div class="page-no">9</div>
  <div class="column" style="left:45px;">
    <h3>Giver:</h3>
    <ul>
      <li>Konkret og aktuel</li>
      <li>Beskrivende fremfor vurderende</li>
      <li>Tag ejerskab, udtryk dig i jeg-form</li>
      <li class="sub">Jeg oplever…</li>
      <li class="sub">Jeg føler…</li>
      <li>Fremadrettet og konstruktiv idé til ændring, rettet mod adfærd</li>
      <li>Efterlad den anden med et valg</li>
    </ul>
    <p class="motto" style="font-weight:700;">OBSERVÈR –KONKRETISÈR –SERVÈR</p>
  </div>
  <div class="column" style="left:309px; width:230px;">
    <h3>Modtager:</h3>
    <ul>
      <li>Vær åben og tag imod</li>
      <li>Lyt og notér hvad der bliver sagt</li>
      <li>Spørg uddybende om du har behov</li>
      <li>Sig tak</li>
      <li>Du har et valg og vælger selv hvad du vil bruge – og hvordan</li>
      <li>Bed om den feedback du (også) ønsker men ikke får</li>
    </ul>
    <p class="motto" style="font-weight:700;">LYT – REFLEKTÈR - SORTER – KVITTÈR</p>
  </div>
  <footer class="footer">
    <div class="brand-pair sm" style="left:12px; top:7px;">
      <span class="brand brand-b"><span class="brand-mark"></span>Nørlund Akademi</span>
      <span class="brand brand-a"><span class="brand-mark"></span>Vedel Rådgivning</span>
    </div>
    <div class="footer-meta"><span>Projektledelse i praksis v. Anders Holm og Sofie Lund</span><span>28-06-2017</span></div>
  </footer>
</section>

<!-- Closing -->
<section class="slide col-b row-5">
  <div class="brand-pair lg" style="left:33px; top:172px;">
    <span class="brand brand-a"><span class="brand-mark"></span>Vedel Rådgivning</span>
    <span class="brand-divider"></span>
    <span class="brand brand-b"><span class="brand-mark"></span>Nørlund Akademi</span>
  </div>
  <div class="rule" style="left:30px; width:268px; top:222px;"></div>
  <p class="thanks abs" style="left:193px; top:234px;">Thank You</p>
</section>

</body>
</html>
```